We want to design total new business card and logo for Kestrel Building Services Ltd

Our company name Kestrel Building Services Ltd. Design new logo and business card , need hi-end luxury style art for architecture and construction industry. The card should simple but stylish. Our business focus on CONNECT tradesman to construction company, help marketing construction company tender oversea projects, managing franchise in construction sector, delivery amazing services to our client, so Logo should show the CONNECTION IDEA, CONNECTING PEOPLE, LUXURY. Visit our website for more information: kestrelgroup-example.co.nz

Target Market(s)

Directors or managers

Industry/Entity Type

Construction Company

Contact Information for Business Card

Name, Title, Mobile, Email, Website

Font styles to use
Serif

Colors

Designer to choose colors to be used in the design.

Requirements
Must have
• Simple and luxury, connection icon
Nice to have
• Special materials, plastic card, look through,...
• Look new ideas.

```html
<!DOCTYPE html>
<html lang="en">
<head>
<meta charset="utf-8">
<title>Kestrel Building Services Ltd – Business Card</title>
<link rel="stylesheet" href="https://fonts.googleapis.com/css2?family=Lato:wght@400;700&display=swap">
<style>
  :root {
    --backdrop: #e6e1da;
    --card-fill: rgba(250, 249, 246, 0.78);
    --card-edge: rgba(255, 255, 255, 0.95);
    --brand-blue: #1f5f8b;
    --text-grey: #575757;
    --brand-grey: #5c5c5c;
  }
  * { margin: 0; padding: 0; box-sizing: border-box; }
  html, body {
    width: 1200px;
    height: 1047px;
    overflow: hidden;
    background: var(--backdrop);
    font-family: "Lato", sans-serif;
  }
  .card {
    position: absolute;
    left: 120px;
    top: 253px;
    width: 960px;
    height: 540px;
    border-radius: 22px;
    background: var(--card-fill);
    border: 2px solid var(--card-edge);
    box-shadow: 0 10px 40px rgba(0, 0, 0, 0.08);
  }
  .brand {
    position: absolute;
    left: 138px;
    top: 222px;
    width: 360px;
    text-align: center;
    color: var(--brand-grey);
    font-size: 28px;
    font-weight: 400;
    line-height: 1.3;
    letter-spacing: 0.5px;
  }
  .divider {
    position: absolute;
    left: 512px;
    top: 132px;
    width: 2px;
    height: 258px;
    background: var(--brand-blue);
  }
  .details {
    position: absolute;
    left: 545px;
    top: 128px;
    color: var(--text-grey);
    font-size: 23px;
    line-height: 1.38;
  }
  .person-name {
    color: var(--brand-blue);
    font-weight: 700;
    font-size: 27px;
    line-height: 1.2;
  }
  .person-title { margin-bottom: 20px; }
  .address { margin-bottom: 20px; }
  .contact-line {
    display: flex;
    align-items: center;
    gap: 10px;
    font-size: 22px;
  }
  .contact-line svg { width: 15px; height: 15px; fill: var(--brand-blue); flex: none; }
  .web-accent { color: var(--brand-blue); }
</style>
</head>
<body>
  <div class="card">
    <div class="brand">Kestrel Building<br>Services Ltd</div>
    <div class="divider"></div>
    <div class="details">
      <div class="person-name">Daniel Hartley</div>
      <div class="person-title">President</div>
      <div class="address">214 Harbour Lane, 3rd Floor<br>Auckland, NZ 1010</div>
      <div class="contact-line">
        <svg viewBox="0 0 24 24" aria-hidden="true"><path d="M6.6 10.8a15.2 15.2 0 0 0 6.6 6.6l2.2-2.2c.3-.3.7-.4 1-.2 1.1.4 2.3.6 3.6.6.6 0 1 .4 1 1V20c0 .6-.4 1-1 1A17 17 0 0 1 3 4c0-.6.4-1 1-1h3.5c.6 0 1 .4 1 1 0 1.3.2 2.5.6 3.6.1.3 0 .7-.2 1z"/></svg>
        <span>021.555.0147</span>
      </div>
      <div class="contact-line">
        <svg viewBox="0 0 24 24" aria-hidden="true"><path d="M2 5h20v14H2z M2 5l10 8 10-8" fill="none" stroke="#1f5f8b" stroke-width="2.4"/></svg>
        <span>info@kestrelgroup-example.co.nz</span>
      </div>
      <div class="contact-line">
        <svg viewBox="0 0 24 24" aria-hidden="true"><circle cx="12" cy="12" r="9.5" fill="none" stroke="#1f5f8b" stroke-width="2"/><path d="M2.5 12h19M12 2.5c-5 5-5 14 0 19M12 2.5c5 5 5 14 0 19" fill="none" stroke="#1f5f8b" stroke-width="1.6"/></svg>
        <span>www.<span class="web-accent">kestrelgroup-example</span>.co.nz</span>
      </div>
    </div>
  </div>
</body>
</html>
```